Pregnancy and Fertility Information Website

Hello Designers,
I need a website which provide tips and information about healthy and happy pregnancy. My website name is KRE medical.

The website should provide all the information needed throughout pregnancy and beyond ranging from pregnancy tracking tools and articles about common pregnancy concerns and what to expect during pregnancy,etc.
The details about first trimester, second trimester and third trimester should be highlighted in the website.

Top Navigation
Home, Fertility, Pregnancy basics, Articles, Tips and News

I'm looking for a simple and clean design which involves captivating images and colors but it shouldn't be crowded. The design must be professional and modern. An easy to navigate layout is a must.

Green, violet, blue and light yellow colors are my favorites but i'm open to other options.

Any questions. Kindly ask

Industry/Entity Type

Medical

```html
<!DOCTYPE html>
<html lang="en">
<head>
<meta charset="utf-8">
<title>KRE Medical – Pregnancy &amp; Fertility</title>
<link rel="stylesheet" href="https://fonts.googleapis.com/css2?family=Fira+Sans:wght@400;600;700&family=Fira+Sans+Condensed:wght@500;600;700&family=Arimo:wght@400&display=swap">
<style>
  :root {
    --teal-dark: #0b5a55;
    --teal-title: #12504f;
    --teal-band: #2e7d78;
    --cyan-frame: #3ad1d6;
    --nav-green: #22c55e;
    --white: #ffffff;
    --page-grey: #f1f1f1;
    --text-dark: #2b2b2b;
    --footer-bg: #232323;
  }
  * { box-sizing: border-box; margin: 0; padding: 0; }
  html, body { width: 1200px; height: 2612px; overflow: hidden; background: var(--white); }
  body { position: relative; font-family: "Fira Sans", sans-serif; color: var(--text-dark); }

  /* Header */
  .site-header { position: absolute; left: 0; top: 0; width: 1200px; height: 125px; background: var(--white); }
  .brand { position: absolute; left: 44px; top: 30px; display: flex; align-items: center; gap: 16px; }
  .brand-dot { width: 58px; height: 58px; border-radius: 50%; background: var(--nav-green); }
  .brand-name { font-family: "Fira Sans", sans-serif; font-weight: 700; font-size: 24px; letter-spacing: 2px; color: var(--nav-green); line-height: 1.1; width: 130px; }
  .social { position: absolute; top: 30px; right: 22px; display: flex; gap: 9px; }
  .social span { width: 33px; height: 33px; border-radius: 50%; display: block; }
  .social .s1 { background: #2d4f8f; } .social .s2 { background: #8c8c8c; } .social .s3 { background: #d9443a; }
  .main-nav { position: absolute; top: 84px; left: 433px; display: flex; font-family: "Fira Sans", sans-serif; font-weight: 700; font-size: 17px; letter-spacing: 2px; }
  .main-nav a { color: var(--nav-green); text-decoration: none; position: relative; margin-right: 36px; }
  .main-nav a:last-child { margin-right: 0; }
  .main-nav a.active { color: var(--teal-dark); }
  .main-nav a.active::after { content: ""; position: absolute; left: -1px; right: -1px; top: 33px; height: 5px; background: var(--teal-dark); }

  /* Hero */
  .hero { position: absolute; left: 0; top: 125px; width: 1200px; height: 641px;
    background: linear-gradient(100deg, #b7aa98 0%, #d8d0c2 30%, #c7c7b4 55%, #a9ae9a 80%, #9aa290 100%); }
  .hero-shade { position: absolute; inset: 0; background: rgba(40,40,40,0.28); }
  .hero-title { position: absolute; top: 285px; width: 100%; text-align: center; font-family: "Arimo", sans-serif; font-size: 35px; letter-spacing: 5px; color: var(--white); }
  .hero-btn { position: absolute; left: 493px; top: 354px; width: 232px; height: 54px; border: 2px solid var(--white); color: var(--white);
    font-family: "Arimo", sans-serif; font-size: 18px; display: flex; align-items: center; justify-content: center; }
  .hero-arrow { position: absolute; top: 321px; width: 30px; height: 30px; }
  .hero-arrow.prev { left: 27px; } .hero-arrow.next { left: 1143px; }

  /* Section headings */
  .section-title { position: absolute; width: 100%; text-align: center; font-family: "Fira Sans Condensed", sans-serif; font-weight: 600; font-size: 30px; letter-spacing: 8px; line-height: 42px; color: var(--teal-title); }

  /* Cards */
  .card { position: absolute; overflow: hidden; }
  .card-photo { position: absolute; inset: 0; }
  .card-frame { position: absolute; left: 8px; top: 8px; right: 8px; bottom: 8px; border: 2px solid var(--cyan-frame); }
  .card-label { position: absolute; left: 22px; bottom: 14px; font-family: "Fira Sans", sans-serif; font-weight: 700; font-size: 22px; letter-spacing: 5px; line-height: 30px; color: var(--white); }
  .card-label.centered { left: 0; right: 0; bottom: auto; top: 102px; text-align: center; }
  .know-more { position: absolute; right: 18px; bottom: 15px; display: flex; align-items: center; gap: 5px; font-family: "Fira Sans Condensed", sans-serif; font-weight: 600; font-size: 10px; color: var(--cyan-frame); }
  .know-more svg { width: 17px; height: 17px; }
  .w1 { left: 92px; width: 288px; } .w2 { left: 395px; width: 408px; } .w3 { left: 817px; width: 292px; }
  .row1 { top: 1001px; height: 284px; } .row2 { top: 1590px; height: 286px; }
  .tone-phone { background: linear-gradient(135deg, #7b5a52 0%, #c9c4bd 45%, #8c6a60 100%); }
  .tone-hands { background: linear-gradient(135deg, #8a5a50 0%, #d2a79a 45%, #6c4a44 100%); }
  .tone-woman { background: linear-gradient(135deg, #c9c7c0 0%, #3b3b44 50%, #e7e4de 100%); }
  .card .tint { position: absolute; inset: 0; background: rgba(20,60,60,0.28); }

  /* Phases band */
  .phases { position: absolute; left: 0; top: 1400px; width: 1200px; height: 572px;
    background: linear-gradient(100deg, #7a8f86 0%, #a6a79a 45%, #8d9b90 100%); }
  .phases-overlay { position: absolute; inset: 0; background: rgba(17,110,104,0.78); }
  .phases .section-title { color: var(--white); top: 59px; }

  /* Memories */
  .memories { position: absolute; left: 0; top: 1972px; width: 1200px; height: 597px; background: var(--page-grey); }
  .memories-panel { position: absolute; left: 92px; top: 0; width: 1017px; height: 597px; background: var(--white); }
  .memories .section-title { top: 40px; letter-spacing: 5px; color: var(--teal-dark); font-weight: 700; }
  .memory-table { position: absolute; left: 92px; top: 116px; width: 1017px; border-collapse: collapse; }
  .memory-table th { height: 53px; background: var(--teal-dark); color: var(--white); font-family: "Fira Sans", sans-serif; font-weight: 700; font-size: 20px; text-align: left; vertical-align: middle; }
  .memory-table td { height: 49px; vertical-align: top; padding-top: 10px; font-size: 13px; font-weight: 700; }
  .memory-table .c1 { padding-left: 9px; width: 511px; }
  .memory-table .c2 { width: 365px; }
  .memory-table .note { display: block; font-weight: 400; font-size: 8px; letter-spacing: 0.5px; margin-top: 2px; }
  .memory-actions { position: absolute; left: 427px; top: 515px; display: flex; gap: 50px; }
  .btn { width: 148px; height: 37px; background: var(--teal-dark); color: var(--white); font-weight: 700; font-size: 14px; letter-spacing: 0.5px; display: flex; align-items: center; justify-content: center; box-shadow: 0 2px 3px rgba(0,0,0,0.25); }

  /* Footer */
  .site-footer { position: absolute; left: 0; top: 2569px; width: 1200px; height: 43px; background: var(--footer-bg); color: var(--nav-green);
    font-weight: 700; font-size: 14px; letter-spacing: 1px; display: flex; align-items: center; justify-content: center; }
</style>
</head>
<body>

<header class="site-header">
  <div class="brand"><span class="brand-dot"></span><span class="brand-name">KRE MEDICAL</span></div>
  <div class="social"><span class="s1"></span><span class="s2"></span><span class="s3"></span></div>
  <nav class="main-nav">
    <a class="active" href="#">HOME</a>
    <a href="#">FERTILITY</a>
    <a href="#">PREGNANCY BASICS</a>
    <a href="#">ARTICLES</a>
    <a href="#">TIPS&amp;NEWS</a>
  </nav>
</header>

<section class="hero" role="img" aria-label="Pregnant woman sitting by a bright window, holding her belly">
  <div class="hero-shade"></div>
  <h1 class="hero-title">GOING THROUGH PREGNANCY</h1>
  <div class="hero-btn">VIEW TIPS</div>
  <svg class="hero-arrow prev" viewBox="0 0 30 30"><circle cx="15" cy="15" r="14" fill="#e6e6e6" opacity="0.85"/><path d="M17.5 9 L11.5 15 L17.5 21" fill="none" stroke="#555" stroke-width="2.5"/></svg>
  <svg class="hero-arrow next" viewBox="0 0 30 30"><circle cx="15" cy="15" r="14" fill="#e6e6e6" opacity="0.85"/><path d="M12.5 9 L18.5 15 L12.5 21" fill="none" stroke="#555" stroke-width="2.5"/></svg>
</section>

<h2 class="section-title" style="top:872px;">THINGS YOU SHOULD<br>KNOW</h2>

<article class="card w1 row1">
  <div class="card-photo tone-phone" role="img" aria-label="Hand holding a phone with a pregnancy tracking app"></div>
  <div class="tint"></div><div class="card-frame"></div>
  <div class="card-label">TRACKING<br>TOOLS</div>
  <div class="know-more"><svg viewBox="0 0 17 17"><circle cx="8.5" cy="8.5" r="8.5" fill="#3ad1d6"/><path d="M7 5 L10.5 8.5 L7 12" fill="none" stroke="#0b3f3f" stroke-width="2"/></svg>KNOW MORE</div>
</article>
<article class="card w2 row1">
  <div class="card-photo tone-hands" role="img" aria-label="Hands forming a heart shape on a pregnant belly"></div>
  <div class="tint"></div><div class="card-frame"></div>
  <div class="card-label">WHAT TO<br>EXPECT?</div>
  <div class="know-more"><svg viewBox="0 0 17 17"><circle cx="8.5" cy="8.5" r="8.5" fill="#3ad1d6"/><path d="M7 5 L10.5 8.5 L7 12" fill="none" stroke="#0b3f3f" stroke-width="2"/></svg>KNOW MORE</div>
</article>
<article class="card w3 row1">
  <div class="card-photo tone-woman" role="img" aria-label="Pregnant woman holding her lower back"></div>
  <div class="tint"></div><div class="card-frame"></div>
  <div class="card-label" style="bottom:6px;">PREGNANCY<br>CONCERN</div>
  <div class="know-more"><svg viewBox="0 0 17 17"><circle cx="8.5" cy="8.5" r="8.5" fill="#3ad1d6"/><path d="M7 5 L10.5 8.5 L7 12" fill="none" stroke="#0b3f3f" stroke-width="2"/></svg>KNOW MORE</div>
</article>

<section class="phases">
  <div role="img" aria-label="Smiling pregnant woman resting at home" style="position:absolute;inset:0;"></div>
  <div class="phases-overlay"></div>
  <h2 class="section-title">DIFFERENT PHASES OF<br>PREGNANCY</h2>
</section>

<article class="card w1 row2">
  <div class="card-photo tone-phone" role="img" aria-label="Phone showing a pregnancy tracker"></div>
  <div class="tint"></div><div class="card-frame"></div>
  <div class="card-label centered">FIRST<br>TRIMESTER</div>
  <div class="know-more"><svg viewBox="0 0 17 17"><circle cx="8.5" cy="8.5" r="8.5" fill="#3ad1d6"/><path d="M7 5 L10.5 8.5 L7 12" fill="none" stroke="#0b3f3f" stroke-width="2"/></svg>KNOW MORE</div>
</article>
<article class="card w2 row2">
  <div class="card-photo tone-hands" role="img" aria-label="Heart-shaped hands on a pregnant belly"></div>
  <div class="tint"></div><div class="card-frame"></div>
  <div class="card-label centered">SECOND<br>TRIMESTER</div>
  <div class="know-more"><svg viewBox="0 0 17 17"><circle cx="8.5" cy="8.5" r="8.5" fill="#3ad1d6"/><path d="M7 5 L10.5 8.5 L7 12" fill="none" stroke="#0b3f3f" stroke-width="2"/></svg>KNOW MORE</div>
</article>
<article class="card w3 row2">
  <div class="card-photo tone-woman" role="img" aria-label="Pregnant woman in late pregnancy"></div>
  <div class="tint"></div><div class="card-frame"></div>
  <div class="card-label centered">THIRD<br>TRIMESTER</div>
  <div class="know-more"><svg viewBox="0 0 17 17"><circle cx="8.5" cy="8.5" r="8.5" fill="#3ad1d6"/><path d="M7 5 L10.5 8.5 L7 12" fill="none" stroke="#0b3f3f" stroke-width="2"/></svg>KNOW MORE</div>
</article>

<section class="memories">
  <div class="memories-panel"></div>
  <h2 class="section-title">MEMORIES</h2>
  <table class="memory-table">
    <thead><tr><th class="c1">MEMORY</th><th class="c2">POSTED BY</th><th>POSTED ON</th></tr></thead>
    <tbody>
      <tr><td class="c1">FIRST MONTH<span class="note">EARLY WEEKS FIRST SCAN NOTES</span></td><td class="c2">RACHEL</td><td>01/04/2017</td></tr>
      <tr><td class="c1">FIRST MONTH<span class="note">EARLY WEEKS FIRST SCAN NOTES</span></td><td class="c2">RACHEL</td><td>01/04/2017</td></tr>
      <tr><td class="c1">FIRST MONTH<span class="note">EARLY WEEKS FIRST SCAN NOTES</span></td><td class="c2">RACHEL</td><td>01/04/2017</td></tr>
      <tr><td class="c1">FIRST MONTH<span class="note">EARLY WEEKS FIRST SCAN NOTES</span></td><td class="c2">RACHEL</td><td>01/04/2017</td></tr>
      <tr><td class="c1">FIRST MONTH<span class="note">EARLY WEEKS FIRST SCAN NOTES</span></td><td class="c2">RACHEL</td><td>01/04/2017</td></tr>
      <tr><td class="c1">FIRST MONTH<span class="note">EARLY WEEKS FIRST SCAN NOTES</span></td><td class="c2">RACHEL</td><td>01/04/2017</td></tr>
    </tbody>
  </table>
  <div class="memory-actions"><div class="btn">VIEW ALL</div><div class="btn">TELL YOURS</div></div>
</section>

<footer class="site-footer">COPYRIGHT © 2017 KRE MEDICAL</footer>

</body>
</html>
```